Creative, Innovative PowerPoint Sales Deck Refresh needed

We are a technology firm in the Dallas, TX area and we need the powerpoint presentation used for our sales calls refreshed. This presentation is used in one of the first meetings we have with potential clients, so we want to make a memorable and positive impact - we want something that sets us apart from everyone else. We need 8 master slide templates created for our sales deck and a series of slides within the example sales deck need to be completely refreshed (slides 31-37 and 43 in the sample ppt file) We want a sales deck that is modern, innovative, creative, memorable and whimsical - NOT a typical boring "business" design. Colors should match or compliment the colors used in our logo. The logo in the footer of the attached sample ppt is old - it should be replaced with the newer logo attached. Please take a look at our website to get an idea of our culture and aesthetic www.quorbinlab.com
Updates

Project Deadline Extended
Reason: We have received several designs we like and we want our entire team to have time to give them full consideration before making a decision.

Target Market(s)

Business executives

Industry/Entity Type

Information Technology

Font styles to use
Sans Serif

Requirements
Must have
• Our logo and LedgerWave logo in footer
• Master Slide Templates
• Rework / redesign of slides 31-37 and 43
Nice to have
• We use Raleway font in a lot of our materials

```html
<!DOCTYPE html>
<html lang="en">
<head>
<meta charset="utf-8">
<title>Slide 43 Design Ideas</title>
<link rel="stylesheet" href="https://fonts.googleapis.com/css2?family=Open+Sans:wght@400;600;700&display=swap">
<style>
  :root{
    --canvas:#141a31;
    --heading:#9fb0aa;
    --slide-bg:#ffffff;
    --brand-blue:#0a5ca8;
    --title-ink:#4a4a4a;
    --rule:#c9d6e3;
    --navy:#0d4a7d;
    --deep-navy:#16386b;
    --steel:#a3b8cc;
    --green:#6cb945;
    --orange:#f07225;
    --charcoal:#262626;
    --black:#161616;
    --grey-dark:#555659;
    --grey-mid:#77797c;
    --arrow:#4a90d6;
  }
  *{box-sizing:border-box;margin:0;padding:0}
  html,body{width:1200px;height:1200px;overflow:hidden;background:var(--canvas)}
  body{position:relative;font-family:"Open Sans",Arial,sans-serif}
  .sheet-title{position:absolute;top:40px;left:0;width:1200px;text-align:center;
    color:var(--heading);font-size:29px;font-weight:600;letter-spacing:.3px}
  .slide{position:absolute;width:582px;height:326px;background:var(--slide-bg);
    border-top:6px solid var(--brand-blue)}
  .slide-title{position:absolute;left:18px;top:7px;right:18px;padding-bottom:3px;
    border-bottom:1px solid var(--rule);color:var(--title-ink);font-size:17.5px;font-weight:600}
  .diagram{position:absolute;left:0;top:0;width:582px;height:320px}
  .footer-rule{position:absolute;left:18px;right:18px;bottom:24px;border-top:1px solid var(--rule)}
  .brand-left{position:absolute;left:20px;bottom:8px;font-size:12.5px;font-weight:700;color:#2d2d2d;letter-spacing:-.2px}
  .brand-right{position:absolute;right:18px;bottom:8px;display:flex;align-items:center;gap:5px;
    font-size:11px;font-weight:700;color:#1d2a44;letter-spacing:.4px}
  .brand-right .mark{width:13px;height:13px;background:#1d2a44}
  .lbl{font-family:"Open Sans",Arial,sans-serif;fill:#fff;text-anchor:middle;font-weight:600}
  .lbl-xs{font-size:5.5px}
  .lbl-sm{font-size:7.5px}
  .hub{font-family:"Open Sans",Arial,sans-serif;fill:#1a1a1a;text-anchor:middle;font-weight:700}
  .r1{top:136px}.r2{top:485px}.r3{top:834px}
  .c1{left:12px}.c2{left:607px}
</style>
</head>
<body>
<h1 class="sheet-title">SLIDE - 43 DESIGN IDEAs</h1>

<svg width="0" height="0" style="position:absolute">
  <defs>
    <radialGradient id="hub-fill" cx="50%" cy="40%" r="60%">
      <stop offset="0" stop-color="#ffffff"/><stop offset=".75" stop-color="#f1f2f3"/><stop offset="1" stop-color="#d9dbde"/>
    </radialGradient>
    <radialGradient id="sector-shade" cx="50%" cy="50%" r="50%">
      <stop offset=".35" stop-color="#000" stop-opacity=".25"/><stop offset=".7" stop-color="#000" stop-opacity="0"/>
    </radialGradient>
    <path id="flow-arrow" d="M-5 -2.4 L0 -2.4 L0 -6 L6 0 L0 6 L0 2.4 L-5 2.4Z" fill="var(--arrow)"/>
    <path id="chevron" d="M -62.6 -92.9 A 112 112 0 0 1 62.6 -92.9 L 51.4 -61.3 L 26.8 -39.8 A 48 48 0 0 0 -26.8 -39.8 L -37.6 -70.6 Z"/>
    <path id="sector" d="M0 0 L -61.1 -84.1 A 104 104 0 0 1 61.1 -84.1 Z"/>
    <g id="ring-arrow">
      <path d="M -72.7 -93 A 118 118 0 0 1 59 -102.2" fill="none" stroke-width="10"/>
      <path d="M71.1 -95.2 L63.5 -110 L54.5 -94.4 Z" stroke="none"/>
    </g>
  </defs>
</svg>

<section class="slide r1 c1">
  <h2 class="slide-title">FIVE KEY AREAS OF USER ADOPTION</h2>
  <svg class="diagram" viewBox="0 0 582 320">
    <g transform="translate(296 176)">
      <circle r="72" fill="url(#hub-fill)"/>
      <g opacity=".95">
        <circle cx="0" cy="-86" r="36" fill="var(--navy)"/>
        <circle cx="81.8" cy="-26.6" r="36" fill="#8ea6bf" opacity=".85"/>
        <circle cx="50.5" cy="69.6" r="36" fill="#5fb43e" opacity=".95"/>
        <circle cx="-50.5" cy="69.6" r="36" fill="var(--orange)"/>
        <circle cx="-81.8" cy="-26.6" r="36" fill="#1f1f1f"/>
      </g>
      <text class="lbl lbl-xs" x="0" y="-84">Alignment</text>
      <text class="lbl lbl-xs" x="84" y="-24">Communication</text>
      <text class="lbl lbl-xs" x="53" y="72">Training</text>
      <text class="lbl lbl-xs" x="-53" y="72">Support</text>
      <text class="lbl lbl-xs" x="-86" y="-24">Measure</text>
      <text class="hub" font-size="8.5" y="-8">Five Key Areas</text>
      <text class="hub" font-size="8.5" y="2.5">Of</text>
      <text class="hub" font-size="8.5" y="13">User Adoption</text>
      <use href="#flow-arrow" transform="rotate(-54) translate(104 0) rotate(90)"/>
      <use href="#flow-arrow" transform="rotate(18) translate(104 0) rotate(90)"/>
      <use href="#flow-arrow" transform="rotate(90) translate(104 0) rotate(90)"/>
      <use href="#flow-arrow" transform="rotate(162) translate(104 0) rotate(90)"/>
      <use href="#flow-arrow" transform="rotate(234) translate(104 0) rotate(90)"/>
    </g>
  </svg>
  <div class="brand-left">quorbinlab</div>
  <div class="brand-right"><span class="mark"></span>LEDGERWAVE</div>
</section>

<section class="slide r1 c2">
  <h2 class="slide-title">Five Key Areas of User Adoption</h2>
  <svg class="diagram" viewBox="0 0 582 320">
    <g transform="translate(296 176)">
      <circle r="72" fill="url(#hub-fill)"/>
      <circle cx="0" cy="-86" r="35" fill="var(--navy)"/>
      <circle cx="81.8" cy="-26.6" r="35" fill="#94abc2" opacity=".85"/>
      <circle cx="50.5" cy="69.6" r="35" fill="var(--black)"/>
      <circle cx="-50.5" cy="69.6" r="35" fill="#5f6164" opacity=".9"/>
      <circle cx="-81.8" cy="-26.6" r="35" fill="#4d4e50" opacity=".9"/>
      <text class="lbl lbl-xs" x="0" y="-84">Alignment</text>
      <text class="lbl lbl-xs" x="84" y="-24">Communication</text>
      <text class="lbl lbl-xs" x="53" y="72">Training</text>
      <text class="lbl lbl-xs" x="-53" y="72">Support</text>
      <text class="lbl lbl-xs" x="-86" y="-24">Measure</text>
      <text class="hub" font-size="8.5" y="-8">Five Key Areas</text>
      <text class="hub" font-size="8.5" y="2.5">Of</text>
      <text class="hub" font-size="8.5" y="13">User Adoption</text>
      <use href="#flow-arrow" transform="rotate(-54) translate(104 0) rotate(90)"/>
      <use href="#flow-arrow" transform="rotate(18) translate(104 0) rotate(90)"/>
      <use href="#flow-arrow" transform="rotate(90) translate(104 0) rotate(90)"/>
      <use href="#flow-arrow" transform="rotate(162) translate(104 0) rotate(90)"/>
      <use href="#flow-arrow" transform="rotate(234) translate(104 0) rotate(90)"/>
    </g>
  </svg>
  <div class="brand-left">quorbinlab</div>
  <div class="brand-right"><span class="mark"></span>LEDGERWAVE</div>
</section>

<section class="slide r2 c1">
  <h2 class="slide-title">Five Key Areas of User Adoption</h2>
  <svg class="diagram" viewBox="0 0 582 320">
    <g transform="translate(296 174)">
      <circle r="126" fill="#f6f7f8" stroke="#e1e3e6" stroke-width="3"/>
      <use href="#chevron" fill="var(--navy)"/>
      <use href="#chevron" fill="#9fb4ca" transform="rotate(72)"/>
      <use href="#chevron" fill="var(--green)" transform="rotate(144)"/>
      <use href="#chevron" fill="var(--orange)" transform="rotate(216)"/>
      <use href="#chevron" fill="var(--charcoal)" transform="rotate(288)"/>
      <circle r="56" fill="url(#sector-shade)"/>
      <circle r="42" fill="#fff" stroke="#e3e5e8" stroke-width="4"/>
      <text class="lbl lbl-sm" x="3" y="-78">Alignment</text>
      <text class="lbl lbl-sm" x="75" y="-22">Communication</text>
      <text class="lbl lbl-sm" x="45" y="76">Training</text>
      <text class="lbl lbl-sm" x="-52" y="72">Support</text>
      <text class="lbl lbl-sm" x="-80" y="-22">Measure</text>
      <text class="hub" font-size="8.5" y="-14">Five</text>
      <text class="hub" font-size="8.5" y="-3">Key Areas</text>
      <text class="hub" font-size="8.5" y="8">Of</text>
      <text class="hub" font-size="8.5" y="19">User Adoption</text>
    </g>
  </svg>
  <div class="brand-left">quorbinlab</div>
  <div class="brand-right"><span class="mark"></span>LEDGERWAVE</div>
</section>

<section class="slide r2 c2">
  <h2 class="slide-title">FIVE KEY AREAS OF USER ADOPTION</h2>
  <svg class="diagram" viewBox="0 0 582 320">
    <g transform="translate(296 170) scale(.93)">
      <circle r="126" fill="#f6f7f8" stroke="#e1e3e6" stroke-width="3"/>
      <use href="#chevron" fill="var(--deep-navy)"/>
      <use href="#chevron" fill="#a0b6cc" transform="rotate(72)"/>
      <use href="#chevron" fill="var(--black)" transform="rotate(144)"/>
      <use href="#chevron" fill="#aabdd0" transform="rotate(216)"/>
      <use href="#chevron" fill="var(--grey-dark)" transform="rotate(288)"/>
      <circle r="56" fill="url(#sector-shade)"/>
      <circle r="42" fill="#fff" stroke="#e3e5e8" stroke-width="4"/>
      <text class="lbl lbl-sm" x="3" y="-78">Alignment</text>
      <text class="lbl lbl-sm" x="75" y="-22">Communication</text>
      <text class="lbl lbl-sm" x="45" y="76">Training</text>
      <text class="lbl lbl-sm" x="-52" y="72">Support</text>
      <text class="lbl lbl-sm" x="-80" y="-22">Measure</text>
      <text class="hub" font-size="9" y="-14">Five</text>
      <text class="hub" font-size="9" y="-3">Key Areas</text>
      <text class="hub" font-size="9" y="8">Of</text>
      <text class="hub" font-size="9" y="19">User Adoption</text>
    </g>
  </svg>
  <div class="footer-rule"></div>
  <div class="brand-left">quorbinlab</div>
  <div class="brand-right"><span class="mark"></span>LEDGERWAVE</div>
</section>

<section class="slide r3 c1">
  <h2 class="slide-title">Five Key Areas of User Adoption</h2>
  <svg class="diagram" viewBox="0 0 582 320">
    <g transform="translate(296 176)">
      <use href="#ring-arrow" fill="var(--navy)" stroke="var(--navy)"/>
      <use href="#ring-arrow" fill="#a3b8cc" stroke="#a3b8cc" transform="rotate(72)"/>
      <use href="#ring-arrow" fill="var(--green)" stroke="var(--green)" transform="rotate(144)"/>
      <use href="#ring-arrow" fill="var(--orange)" stroke="var(--orange)" transform="rotate(216)"/>
      <use href="#ring-arrow" fill="var(--charcoal)" stroke="var(--charcoal)" transform="rotate(288)"/>
      <circle r="107" fill="none" stroke="#fff" stroke-width="4"/>
      <use href="#sector" fill="var(--navy)"/>
      <use href="#sector" fill="#a7bacd" transform="rotate(72)"/>
      <use href="#sector" fill="var(--green)" transform="rotate(144)"/>
      <use href="#sector" fill="var(--orange)" transform="rotate(216)"/>
      <use href="#sector" fill="#2a2a2a" transform="rotate(288)"/>
      <circle r="62" fill="url(#sector-shade)"/>
      <circle r="32" fill="#fff"/>
      <text class="lbl lbl-sm" x="0" y="-68">Alignment</text>
      <text class="lbl lbl-sm" x="64" y="-18">Communication</text>
      <text class="lbl lbl-sm" x="42" y="59">Training</text>
      <text class="lbl lbl-sm" x="-38" y="59">Support</text>
      <text class="lbl lbl-sm" x="-64" y="-20">Measure</text>
      <text class="hub" font-size="7.5" y="-12">Five</text>
      <text class="hub" font-size="7.5" y="-2.5">Key Areas</text>
      <text class="hub" font-size="7.5" y="7">Of</text>
      <text class="hub" font-size="7.5" y="16.5">User Adoption</text>
    </g>
  </svg>
  <div class="brand-left">quorbinlab</div>
  <div class="brand-right"><span class="mark"></span>LEDGERWAVE</div>
</section>

<section class="slide r3 c2">
  <h2 class="slide-title">FIVE KEY AREAS OF USER ADOPTION</h2>
  <svg class="diagram" viewBox="0 0 582 320">
    <g transform="translate(296 176)">
      <use href="#ring-arrow" fill="var(--navy)" stroke="var(--navy)"/>
      <use href="#ring-arrow" fill="#a9bdd1" stroke="#a9bdd1" transform="rotate(72)"/>
      <use href="#ring-arrow" fill="#1f1f1f" stroke="#1f1f1f" transform="rotate(144)"/>
      <use href="#ring-arrow" fill="var(--grey-mid)" stroke="var(--grey-mid)" transform="rotate(216)"/>
      <use href="#ring-arrow" fill="var(--grey-dark)" stroke="var(--grey-dark)" transform="rotate(288)"/>
      <circle r="107" fill="none" stroke="#fff" stroke-width="4"/>
      <use href="#sector" fill="var(--navy)"/>
      <use href="#sector" fill="#a9bdd1" transform="rotate(72)"/>
      <use href="#sector" fill="#1f1f1f" transform="rotate(144)"/>
      <use href="#sector" fill="#7b7d80" transform="rotate(216)"/>
      <use href="#sector" fill="var(--grey-dark)" transform="rotate(288)"/>
      <circle r="62" fill="url(#sector-shade)"/>
      <circle r="32" fill="#fff"/>
      <text class="lbl lbl-sm" x="0" y="-68">Alignment</text>
      <text class="lbl lbl-sm" x="64" y="-18">Communication</text>
      <text class="lbl lbl-sm" x="42" y="59">Training</text>
      <text class="lbl lbl-sm" x="-38" y="59">Support</text>
      <text class="lbl lbl-sm" x="-64" y="-20">Measure</text>
      <text class="hub" font-size="7.5" y="-12">Five</text>
      <text class="hub" font-size="7.5" y="-2.5">Key Areas</text>
      <text class="hub" font-size="7.5" y="7">Of</text>
      <text class="hub" font-size="7.5" y="16.5">User Adoption</text>
    </g>
  </svg>
  <div class="brand-left">quorbinlab</div>
  <div class="brand-right"><span class="mark"></span>LEDGERWAVE</div>
</section>
</body>
</html>
```